Larkwell Bend responsive web design

We need a responsive, bootstrap compatible (but design only - PSD files) website design for a fly fishing shop and guide service.

Design should be very clean. Home Page design + interior page design please.

Possible Home Page Content:
Slide Show
Highlight Three Features: Guided Trips, Fly Shop, Missouri River
About

Thank you and good luck!

Industry/Entity Type

Shop

Requirements
Must have
• This will be used on Bootstrap CMS so needs 12 column bootstrap measurements.

DESIGN ONLY NEEDED (clean PSD files), no programming required.
Need a Home Page layout and secondary page layout

Must show use of the following:
H1 - H5 font uses
link color
Dropdown for navigation bar
Button example
Should not have
• No cutout images, this will be part of CMS and client needs to be able to update most content without knowing photoshop.

```html
<!DOCTYPE html>
<html lang="en">
<head>
<meta charset="utf-8">
<title>Larkwell Bend</title>
<link href="https://fonts.googleapis.com/css2?family=Arimo:wght@400;700&family=Dancing+Script:wght@500&display=swap" rel="stylesheet">
<style>
:root{
  --navy:#0f2530;
  --navy-deep:#0a1a22;
  --gold:#c9a100;
  --green:#1e7a2a;
  --sand:#e2c9b3;
  --cream:#f6f2ec;
  --ink:#222;
  --footer:#0b0b0b;
  --white:#ffffff;
}
*{box-sizing:border-box;margin:0;padding:0}
html,body{width:720px;height:1200px;overflow:hidden}
body{font-family:"Arimo",Arial,sans-serif;color:var(--ink);background:var(--white);position:relative}
.page{position:relative;width:720px;height:1200px}

/* hero */
.hero{position:absolute;left:0;top:0;width:720px;height:402px;background:var(--navy)}
.hero-photo{position:absolute;left:0;top:60px;width:720px;height:342px;
  background:linear-gradient(100deg,#5c6a6a 0%,#8a7a62 25%,#b9a58a 45%,#7a6a55 62%,#4d5a4a 80%,#6a7c70 100%)}
.brand{position:absolute;left:15px;top:10px;width:203px;height:162px;background:var(--navy);
  display:flex;align-items:center;justify-content:center;gap:8px}
.brand-dot{width:14px;height:14px;background:var(--gold);border-radius:50%;flex:none}
.brand-name{font-size:24px;font-weight:700;color:var(--gold);white-space:nowrap}
.nav{position:absolute;top:15px;right:15px;display:flex;gap:11px}
.nav a{display:block;height:18px;padding:0 6px;font-size:10px;line-height:18px;color:#111;background:var(--white);
  text-decoration:none;border-radius:2px;font-weight:700}
.nav a.active{background:var(--gold);color:var(--white)}
.newsletter{position:absolute;left:462px;top:171px;width:228px;height:30px;background:rgba(40,40,30,.55);
  border:2px solid #8a7a68;color:var(--white);font-size:15px;font-weight:700;line-height:26px;padding-left:12px}
.submit{position:absolute;left:575px;top:213px;width:115px;height:32px;background:var(--green);color:var(--white);
  font-size:12px;font-weight:700;letter-spacing:1px;text-align:center;line-height:32px;border-radius:2px}
.welcome{position:absolute;left:0;top:330px;width:720px;height:72px;background:rgba(10,26,34,.78);
  color:var(--white);font-size:32px;font-weight:700;font-variant:small-caps;text-align:right;padding-right:22px;line-height:72px}

/* offer */
.offer{position:absolute;left:0;top:402px;width:720px;height:375px;background:var(--sand)}
.search{position:absolute;left:483px;top:21px;width:167px;height:29px;background:var(--cream);font-size:14px;
  font-weight:700;line-height:29px;padding-left:10px;color:#333}
.search-btn{position:absolute;left:655px;top:19px;width:34px;height:33px;background:var(--cream)}
.script{font-family:"Dancing Script",cursive;font-weight:500;color:#333}
.offer h2{position:absolute;left:55px;top:42px;font-size:44px}
.card{position:absolute;top:126px;width:222px;height:220px}
.card svg.frame{position:absolute;left:0;top:0}
.card-head{position:absolute;left:0;top:24px;width:100%;height:36px;display:flex;align-items:center;justify-content:center;gap:10px;
  color:var(--white);font-size:20px;font-variant:small-caps;letter-spacing:.5px}
.card-head.two-line{top:18px;height:44px;line-height:1.05;text-align:center}
.card p{position:absolute;left:20px;right:20px;top:70px;color:var(--white);font-size:8px;line-height:13px;
  text-transform:uppercase;text-align:center}

/* testimonials */
.testimonials{position:absolute;left:0;top:777px;width:720px;height:288px;background:var(--cream)}
.testimonials h2{position:absolute;left:55px;top:24px;font-size:42px}
.quote-card{position:absolute;left:55px;top:88px;width:208px;height:171px;border:1.5px solid #777;background:var(--white);
  display:flex;align-items:center;justify-content:center;gap:8px}
.quote-card .brand-name{color:var(--navy)}
.quote-card .brand-dot{background:var(--navy)}
.quote-bar{position:absolute;left:300px;top:90px;width:5px;height:87px;background:var(--gold)}
.quote{position:absolute;left:316px;top:86px;width:362px;font-size:9.5px;line-height:20.5px;color:#333}

/* footer */
.footer{position:absolute;left:0;top:1065px;width:720px;height:135px;background:var(--footer);color:var(--white);font-size:8px}
.footer ul{position:absolute;top:21px;list-style:none}
.footer li{height:20px;color:var(--white)}
.footer .strong{font-weight:700}
.copyright{position:absolute;left:57px;top:117px}
.privacy{position:absolute;left:637px;top:117px}
</style>
</head>
<body>
<div class="page">

  <header class="hero">
    <div class="hero-photo" role="img" aria-label="Photo of a fly fishing guide in cap and sunglasses on the river bank"></div>
    <div class="brand"><span class="brand-dot"></span><span class="brand-name">Larkwell Bend</span></div>
    <nav class="nav">
      <a class="active" href="#">Home</a>
      <a href="#">About us</a>
      <a href="#">Contact us</a>
    </nav>
    <div class="newsletter">Receive our news letter</div>
    <div class="submit">SUBMIT</div>
    <h1 class="welcome">Welcome to Larkwell Bend</h1>
  </header>

  <section class="offer">
    <div class="search">Search</div>
    <div class="search-btn">
      <svg width="34" height="33" viewBox="0 0 34 33"><circle cx="15" cy="14" r="6" fill="none" stroke="#111" stroke-width="2.5"/><line x1="19.5" y1="18.5" x2="25" y2="24" stroke="#111" stroke-width="3"/></svg>
    </div>
    <h2 class="script">We offer</h2>

    <article class="card" style="left:15px">
      <svg class="frame" width="222" height="220" viewBox="0 0 222 220"><path d="M2 30 L30 2 H192 L220 30 V208 Q220 218 210 218 H12 Q2 218 2 208 Z" fill="var(--navy)" stroke="#c9d2d6" stroke-width="2"/><path d="M7 32 L32 7 H190 L215 32 V206 Q215 213 208 213 H14 Q7 213 7 206 Z" fill="none" stroke="#5f7480" stroke-width="1"/></svg>
      <div class="card-head"><svg width="18" height="26" viewBox="0 0 18 26"><path d="M9 1 C4 1 1 5 1 9 C1 15 9 25 9 25 C9 25 17 15 17 9 C17 5 14 1 9 1Z" fill="#fff"/><circle cx="9" cy="9" r="3" fill="var(--navy)"/></svg>Guided Trips</div>
      <p>A long established fact that a reader will be distracted by the readable content of a page when looking at its layout. The point of using Lorem Ipsum is that it has a more-or-less normal distribution of letters, as opposed to using 'Content here, content here', making it look like readable English. Many desktop publishing ...</p>
    </article>

    <article class="card" style="left:250px">
      <svg class="frame" width="222" height="220" viewBox="0 0 222 220"><path d="M2 30 L30 2 H192 L220 30 V208 Q220 218 210 218 H12 Q2 218 2 208 Z" fill="var(--navy)" stroke="#c9d2d6" stroke-width="2"/><path d="M7 32 L32 7 H190 L215 32 V206 Q215 213 208 213 H14 Q7 213 7 206 Z" fill="none" stroke="#5f7480" stroke-width="1"/></svg>
      <div class="card-head"><svg width="28" height="22" viewBox="0 0 28 22"><path d="M9 8 L14 2 L19 8" fill="none" stroke="#fff" stroke-width="2"/><path d="M2 8 H26 L23 20 H5 Z" fill="none" stroke="#fff" stroke-width="2"/><line x1="10" y1="11" x2="10" y2="17" stroke="#fff" stroke-width="1.5"/><line x1="14" y1="11" x2="14" y2="17" stroke="#fff" stroke-width="1.5"/><line x1="18" y1="11" x2="18" y2="17" stroke="#fff" stroke-width="1.5"/></svg>Fly Shop</div>
      <p>A long established fact that a reader will be distracted by the readable content of a page when looking at its layout. The point of using Lorem Ipsum is that it has a more-or-less normal distribution of letters, as opposed to using 'Content here, content.....</p>
    </article>

    <article class="card" style="left:485px">
      <svg class="frame" width="222" height="220" viewBox="0 0 222 220"><path d="M2 30 L30 2 H192 L220 30 V208 Q220 218 210 218 H12 Q2 218 2 208 Z" fill="var(--navy)" stroke="#c9d2d6" stroke-width="2"/><path d="M7 32 L32 7 H190 L215 32 V206 Q215 213 208 213 H14 Q7 213 7 206 Z" fill="none" stroke="#5f7480" stroke-width="1"/></svg>
      <div class="card-head two-line"><svg width="34" height="34" viewBox="0 0 34 34"><circle cx="17" cy="17" r="15" fill="none" stroke="#fff" stroke-width="2.5"/><path d="M17 7 L21 17 L17 27 L13 17 Z" fill="#fff"/><circle cx="17" cy="17" r="2.5" fill="var(--navy)"/></svg><span>Missouri<br>River</span></div>
      <p>A long established fact that a reader will be distracted by the readable content of a page when looking at its layout. The point of using Lorem Ipsum is that it has a more-or-less normal distribution of letters, as opposed to using 'Content here, content here', making it look like readable...</p>
    </article>
  </section>

  <section class="testimonials">
    <h2 class="script">Testmonials</h2>
    <div class="quote-card"><span class="brand-dot"></span><span class="brand-name">Larkwell Bend</span></div>
    <div class="quote-bar"></div>
    <p class="quote">Long established fact that a reader will be distracted by the readable content of a page when looking at its layout. The point of using Lorem Ipsum is that it has a more-or-less normal distribution of letters, as opposed to using 'Content here, content here', making it look like readable English. Many desktop publishing ...<br>&nbsp;a long established fact that a reader will be distracted by the readable content of a page when looking at its layout. The point of using Lorem Ipsum is that it has a more-or-less normal distribution of letters, as opposed to using 'Content here, content here.</p>
  </section>

  <footer class="footer">
    <ul style="left:108px"><li class="strong">Getting started now</li><li>FAQs</li><li>Meet the guides</li></ul>
    <ul style="left:316px"><li>our pricing policy</li><li>Download guide maps</li></ul>
    <ul style="left:519px"><li>email: sales@ larkwell bend</li><li>Phone: +2550134</li><li>Montana</li></ul>
    <span class="copyright">@2014 larkwell bend</span>
    <span class="privacy">private policy</span>
  </footer>

</div>
</body>
</html>
```